Computer business require Thank you flyer to include in shipments

We ship computers (mainly laptops, tablets) to customers, most shipments are single unit in a box, we like to include in each box one page flyer as a Thank you note, and also mention in the note that for any reason if the buyer is not satisfied with the purchase or they wish to return the item they can contact us and will take care of any issue.
am thinking to have the design reflect a modern look, also with some color possibly to attract the customer attention and make them read the note, as some people tend to not read paper included in shipments. I will include the content that we like to be on the flyer, however we are open to suggestions either to add more text or how to layout the contents on the page. We also have a company logo that we would like to have it on the flyer.

Target Market(s)

End user, business buyers, wholesalers

Industry/Entity Type

Business

Font styles to use
Sans Serif
Other font styles liked:
• maybe even arial or times roman, a font that would be commonly used for a flyer easy readable

Colors
3377b5
f04a50
e667a6
b868aa
33a6d7
0792cd
ec1f27

Requirements
Must have
• Company logo
Nice to have
• Possible the address somewhere on the bottom of the page either left or right or one line at the end, depending how would look with the layout.
• Not too sure about color, most likely blue similar to our logo colors would be first choice, I was also thinking just to catch buyers attention when they open the package should we do it maybe red or even pink which would be softer tone possibly making it interesting for buyer to read. I know some colors would bring more attention to say "READ ME". Or maybe I'll have 2 flyers in different colors and sent to buyers accordingly based on the gender.
Should not have
• Somehow I did not realize we had added the note section on the content, I like to remove that part that mention about "Read Below Notes...." then the two paragraph that follow about technical guide. I just want this flyer be a Thank you note as well as inform buyers to contact us directly if they have issue.

```html
<!DOCTYPE html>
<html lang="en">
<head>
<meta charset="utf-8">
<title>Thank You Flyer – Quillmere Supply</title>
<link href="https://fonts.googleapis.com/css2?family=Arimo:wght@400;700&display=swap" rel="stylesheet">
<style>
  :root {
    --brand-blue: #0792cd;
    --deep-blue: #3377b5;
    --sky-blue: #33a6d7;
    --pale-blue: #d6ecf8;
    --alert-red: #ec1f27;
    --ink: #1f2a33;
    --muted: #6b7780;
    --paper: #ffffff;
  }
  * { margin: 0; padding: 0; box-sizing: border-box; }
  html, body { width: 900px; height: 1200px; overflow: hidden; background: var(--paper); }
  body { font-family: "Arimo", Arial, sans-serif; color: var(--ink); }

  .flyer { position: relative; width: 900px; height: 1200px; overflow: hidden; background: var(--paper); }

  .header-art {
    position: absolute; top: 0; right: 0; width: 520px; height: 190px;
    border-bottom-left-radius: 260px 190px;
    background: linear-gradient(135deg, #eef7fc 0%, var(--pale-blue) 55%, #a9d6ef 100%);
  }

  .brand { position: absolute; left: 55px; top: 48px; }
  .brand-name { font-size: 30px; font-weight: 700; color: var(--ink); letter-spacing: 0.5px; line-height: 1; }
  .brand-tagline { margin-top: 12px; font-size: 15px; color: var(--muted); }

  .read-me {
    position: absolute; left: 478px; top: 190px;
    font-size: 74px; font-weight: 700; color: var(--alert-red); letter-spacing: 2px; line-height: 1;
  }

  .letter {
    position: absolute; left: 55px; top: 290px; width: 790px;
    font-size: 16.5px; line-height: 20px;
  }
  .letter p { margin-bottom: 18px; }
  .letter p.tight { margin-bottom: 0; }

  .tile-band {
    position: absolute; left: 0; top: 840px; width: 900px; height: 230px;
    background: linear-gradient(90deg, var(--deep-blue) 0%, var(--brand-blue) 28%, var(--sky-blue) 48%, #cfe7f5 72%, #f1f5f8 100%);
  }

  .footer {
    position: absolute; left: 0; bottom: 0; width: 900px; height: 130px;
    background: linear-gradient(180deg, var(--brand-blue), var(--deep-blue));
    color: #fff; display: flex; align-items: center; padding: 0 40px 0 55px; gap: 28px;
    font-size: 13px; line-height: 17px;
  }
  .contact { display: flex; align-items: flex-start; gap: 10px; }
  .contact svg { flex: none; width: 26px; height: 26px; }
  .contact-address { width: 200px; }
  .contact-phone { width: 270px; white-space: nowrap; }
  .contact-web { flex-direction: column; gap: 8px; white-space: nowrap; }
  .contact-web .line { display: flex; align-items: center; gap: 10px; }
  .contact-web svg { width: 22px; height: 22px; }
</style>
</head>
<body>
<main class="flyer">
  <div class="header-art" role="img" aria-label="Light blue rounded-tile pattern"></div>

  <header class="brand">
    <div class="brand-name">QUILLMERE SUPPLY</div>
    <div class="brand-tagline">Computer &amp; Electronics Wholesaler</div>
  </header>

  <h1 class="read-me">READ ME</h1>

  <section class="letter">
    <p>Dear Customer,</p>
    <p>Thank you for your purchase, we very much appreciate your business, it has been a pleasure serving you.</p>
    <p class="tight">Customer satisfaction is our #1 priority; at the same time our commitment is to provide quality products with exceptional customer service.</p>
    <p class="tight">We hope you have received your item in good condition and in a timely manner, please inspect the contents of the box to make sure no damage during transit, if any damage found please report to us immediately.</p>
    <p>Please keep the original packaging just in case you would require to return the item.</p>
    <p class="tight">We respectfully ask if you are in any way dissatisfied with your purchase, either having remorse, change of mind or an issue with the item received, please contact us directly through email at customerservice@quillmeresupply.com or call us Toll Free at (888) 555-0142 and give us the opportunity to make it right for you, we are committed to ensuring that you are completely satisfied with your purchase.</p>
    <p>Please note for immediate assistance contact us during business hours Monday through Friday between 8am to 4pm (California time), appreciate your patience until we solve any issue, we value your business and would like to address your concern as quickly as possible.</p>
    <p>If you have been satisfied with our product and service we would greatly appreciate a moment of your time to leave your feedback for this transaction on the marketplace site where you did the purchase, your opinion would allow us to maintain our high standards in providing a wonderful buying experience for all customers.</p>
  </section>

  <div class="tile-band" role="img" aria-label="Band of rounded square tiles shading from deep blue to pale grey"></div>

  <footer class="footer">
    <div class="contact contact-address">
      <svg viewBox="0 0 24 24" aria-hidden="true"><path fill="#fff" d="M12 2a7 7 0 0 0-7 7c0 5 7 13 7 13s7-8 7-13a7 7 0 0 0-7-7zm0 9.5A2.5 2.5 0 1 1 12 6.5a2.5 2.5 0 0 1 0 5z"/></svg>
      <div>Quillmere Supply<br>2450 W. Harbor Ave.<br>Lakeview, CA 90000</div>
    </div>
    <div class="contact contact-phone">
      <svg viewBox="0 0 24 24" aria-hidden="true"><path fill="#fff" d="M6.6 10.8a15.1 15.1 0 0 0 6.6 6.6l2.2-2.2a1 1 0 0 1 1-.25 11.4 11.4 0 0 0 3.6.57 1 1 0 0 1 1 1V20a1 1 0 0 1-1 1A17 17 0 0 1 3 4a1 1 0 0 1 1-1h3.5a1 1 0 0 1 1 1c0 1.25.2 2.45.57 3.6a1 1 0 0 1-.25 1z"/></svg>
      <div>1-888-555-0142 (TOLL FREE)<br>818 555-0176 (INTERNATIONAL)<br>818 555-0190 (FAX)</div>
    </div>
    <div class="contact contact-web">
      <div class="line">
        <svg viewBox="0 0 24 24" aria-hidden="true"><rect x="2" y="5" width="20" height="14" rx="2" fill="#fff"/><path d="M3 6l9 7 9-7" fill="none" stroke="#3377b5" stroke-width="1.6"/></svg>
        <span>sales@quillmeresupply.com</span>
      </div>
      <div class="line">
        <svg viewBox="0 0 24 24" aria-hidden="true"><circle cx="12" cy="12" r="9.5" fill="none" stroke="#fff" stroke-width="1.6"/><path d="M2.5 12h19M12 2.5c3 3 3 16 0 19M12 2.5c-3 3-3 16 0 19" fill="none" stroke="#fff" stroke-width="1.4"/></svg>
        <span>www.quillmeresupply.com</span>
      </div>
    </div>
  </footer>
</main>
</body>
</html>
```